Hochzeitseinladung
Zielgruppe
Gastronomie - Zielgruppe ist ein Hochzeitspaar, welches bei uns feiert. Wir dürfen Ihre Hochzeitseinladung entwerfen.
Aufgabenstellung
Den Textvorschlag des Brautpaares findet Ihr im Anhang. Das Thema der Hochzeit ist AMORE.
1. Die Hochzeitseinladung darf gerne kreativ gestaltet sein, vielleicht in Form des Moodboard-Bildes im Anhang? Mattes hat braune Haare und Locken und Doreen lange braune Haare. Beide tragen eine Brille.
Das Hochzeitspaar hat noch einen kleinen braunen Zwergpudel 'Fips', vielleicht findet er auch noch Platz auf der Einladungskarte ;-).
2. Als Alternativ-Vorschlag wäre ein klassisches Design auf zB geprägtem Papier toll.
3. Etwas Schlichtes mit einem Neon-Accessoire würde das Hochzeitspaar auch gut finden. Zb brauner Karton mit einem Neonband.

```html
<!DOCTYPE html>
<html lang="de">
<head>
<meta charset="utf-8">
<title>Hochzeitseinladung Doreen &amp; Mattes</title>
<link href="https://fonts.googleapis.com/css2?family=Abril+Fatface&family=Cormorant+Garamond:wght@500;600&family=Roboto+Slab:wght@400;700&display=swap" rel="stylesheet">
<style>
  :root {
    --backdrop: #e8e7e5;
    --paper: #f4f7f6;
    --paper-wash: #e6eeeb;
    --ink: #222222;
    --ink-soft: #4a4a4a;
    --leaf: #8fb39f;
    --leaf-dark: #5f8a73;
    --suit: #3a3a3a;
    --hair: #6b5646;
    --dress: #efe8dc;
  }
  * { box-sizing: border-box; margin: 0; padding: 0; }
  html, body { width: 1200px; height: 844px; overflow: hidden; background: var(--backdrop); }
  body { position: relative; color: var(--ink); }

  .card {
    position: absolute;
    top: 92px;
    width: 460px;
    height: 660px;
    background: linear-gradient(180deg, var(--paper) 0%, var(--paper-wash) 55%, var(--paper) 100%);
    box-shadow: 0 6px 18px rgba(0,0,0,.12);
    overflow: hidden;
  }
  .card--front { left: 100px; }
  .card--schedule { left: 640px; }

  .foliage {
    position: absolute;
    background: radial-gradient(ellipse at center, var(--leaf) 0%, rgba(143,179,159,.55) 45%, rgba(143,179,159,0) 72%);
  }

  /* Front card */
  .front__foliage-top { left: 110px; top: -40px; width: 240px; height: 150px; }
  .front__foliage-left { left: 0; bottom: 0; width: 120px; height: 230px; }
  .front__foliage-right { right: -10px; bottom: 40px; width: 120px; height: 240px; }
  .front__text { position: absolute; top: 118px; left: 0; width: 100%; text-align: center; }
  .tagline { font: 600 15px "Cormorant Garamond", serif; letter-spacing: .28em; }
  .couple-names { font: 44px/1.1 "Abril Fatface", serif; margin-top: 8px; }
  .divider { display: block; margin: 10px auto; }
  .date { font: 600 17px "Cormorant Garamond", serif; letter-spacing: .04em; text-transform: uppercase; }
  .place { font: 600 13px "Cormorant Garamond", serif; letter-spacing: .3em; }
  .couple-art {
    position: absolute; left: 110px; bottom: 0; width: 270px; height: 300px;
    background: linear-gradient(90deg, var(--suit) 0%, var(--suit) 52%, var(--hair) 53%, var(--dress) 100%);
    border-radius: 120px 120px 0 0;
  }

  /* Schedule card */
  .schedule__foliage-top { left: -30px; top: -30px; width: 200px; height: 200px; }
  .schedule__foliage-bottom { right: -30px; bottom: 20px; width: 170px; height: 240px; }
  .caps { font-family: "Cormorant Garamond", serif; text-transform: uppercase; text-align: center; }
  .theme { position: absolute; top: 34px; width: 100%; font-weight: 600; font-size: 15px; letter-spacing: .22em; }
  .theme-divider { position: absolute; top: 62px; left: 170px; }
  .dresscode { position: absolute; top: 88px; width: 100%; font-weight: 600; font-size: 15px; letter-spacing: .22em; }
  .dresscode-lines { position: absolute; top: 120px; width: 100%; font-size: 12px; letter-spacing: .18em; line-height: 1.75; color: var(--ink-soft); }
  .timeline-title { position: absolute; top: 170px; width: 100%; font-weight: 600; font-size: 16px; letter-spacing: .24em; }

  .timeline { position: absolute; left: 0; top: 0; }
  .event { position: absolute; width: 150px; text-align: center; font: 400 9px/1.35 "Roboto Slab", serif; letter-spacing: .08em; text-transform: uppercase; color: var(--ink-soft); }
  .event strong { display: block; color: var(--ink); font-weight: 700; }
  .event__icon { display: block; width: 34px; height: 34px; margin: 0 auto 6px; border-radius: 50%; background: #d9dedc; border: 1px solid #9aa09d; }

  .notes { position: absolute; left: 94px; top: 574px; width: 300px; font: 400 7px/1.4 "Roboto Slab", serif; text-transform: uppercase; letter-spacing: .06em; color: var(--ink-soft); }
  .notes p { margin-bottom: 12px; }
</style>
</head>
<body>

<section class="card card--front" aria-label="Einladung Vorderseite">
  <div class="foliage front__foliage-top" role="img" aria-label="Eukalyptuszweige"></div>
  <div class="front__text">
    <p class="tagline">WE SAY YES</p>
    <h1 class="couple-names">Doreen &amp; Mattes</h1>
    <svg class="divider" width="150" height="8" viewBox="0 0 150 8"><line x1="0" y1="4" x2="150" y2="4" stroke="#222" stroke-width="1"/><circle cx="63" cy="4" r="1.6"/><circle cx="75" cy="4" r="2.6"/><circle cx="87" cy="4" r="1.6"/></svg>
    <p class="date">Samstag, 20 April 2024</p>
    <svg class="divider" width="150" height="8" viewBox="0 0 150 8"><line x1="0" y1="4" x2="150" y2="4" stroke="#222" stroke-width="1"/><circle cx="63" cy="4" r="1.6"/><circle cx="75" cy="4" r="2.6"/><circle cx="87" cy="4" r="1.6"/></svg>
    <p class="place">ROSENAU</p>
    <svg class="divider" width="150" height="8" viewBox="0 0 150 8"><line x1="0" y1="4" x2="150" y2="4" stroke="#222" stroke-width="1"/><circle cx="63" cy="4" r="1.6"/><circle cx="75" cy="4" r="2.6"/><circle cx="87" cy="4" r="1.6"/></svg>
  </div>
  <div class="foliage front__foliage-left" role="img" aria-label="Eukalyptuszweige"></div>
  <div class="foliage front__foliage-right" role="img" aria-label="Eukalyptuszweige"></div>
  <div class="couple-art" role="img" aria-label="Illustration des Brautpaares von hinten, Arm in Arm"></div>
</section>

<section class="card card--schedule" aria-label="Einladung Rückseite">
  <div class="foliage schedule__foliage-top" role="img" aria-label="Eukalyptuszweige"></div>
  <div class="foliage schedule__foliage-bottom" role="img" aria-label="Eukalyptuszweige"></div>

  <h2 class="caps theme">Thema: Amore</h2>
  <svg class="theme-divider" width="120" height="8" viewBox="0 0 120 8"><line x1="0" y1="4" x2="120" y2="4" stroke="#222"/><circle cx="50" cy="4" r="1.5"/><circle cx="60" cy="4" r="2.4"/><circle cx="70" cy="4" r="1.5"/></svg>
  <h2 class="caps dresscode">Dresscode</h2>
  <p class="caps dresscode-lines">Tagsüber: Cocktail - Look<br>Abends: Elegant (Abendkleider/Anzüge)</p>
  <h2 class="caps timeline-title">Zeitplan</h2>

  <svg class="timeline" width="460" height="560" viewBox="0 0 460 560" aria-hidden="true">
    <g stroke="#222" stroke-width="1.4" fill="#222">
      <line x1="230" y1="232" x2="230" y2="500"/>
      <circle cx="230" cy="232" r="5"/>
      <circle cx="230" cy="286" r="5"/>
      <circle cx="230" cy="338" r="5"/>
      <circle cx="230" cy="390" r="5"/>
      <circle cx="230" cy="442" r="5"/>
      <circle cx="230" cy="500" r="5"/>
    </g>
    <g stroke="#222" stroke-width="1" stroke-dasharray="3 2">
      <line x1="160" y1="286" x2="225" y2="286"/>
      <line x1="235" y1="338" x2="300" y2="338"/>
      <line x1="160" y1="390" x2="225" y2="390"/>
      <line x1="235" y1="442" x2="300" y2="442"/>
      <line x1="160" y1="500" x2="225" y2="500"/>
    </g>
  </svg>

  <div class="event" style="left:265px; top:210px;"><span class="event__icon" role="img" aria-label="Kirche"></span>13:30 Uhr<strong>Eintreffen</strong>Lindenhof Kloster</div>
  <div class="event" style="left:55px; top:268px;"><span class="event__icon" role="img" aria-label="Eheringe"></span>13:45 Uhr<strong>Standesamtliche Trauung</strong></div>
  <div class="event" style="left:265px; top:320px;"><span class="event__icon" role="img" aria-label="Sektgläser"></span>14:30 Uhr<strong>Sektempfang</strong>Weinstube Kelch<br>(Ahornweg 4)</div>
  <div class="event" style="left:55px; top:372px;"><span class="event__icon" role="img" aria-label="Kaffeepause"></span>16 Uhr<strong>Kurze Pause</strong></div>
  <div class="event" style="left:265px; top:424px;"><span class="event__icon" role="img" aria-label="Teller mit Besteck"></span>18:30 Uhr<strong>Eintreffen</strong>Gasthaus Alte Mühle<br>(Brunnenplatz 45)</div>
  <div class="event" style="left:55px; top:482px;"><span class="event__icon" role="img" aria-label="Discokugel"></span>Ab 18:30 Uhr<strong>Vegetarisches Flying Dinner, Cocktails und Party</strong></div>

  <div class="notes">
    <p>✦ Im Standesamt stehen leider nur 20 Plätze zur Verfügung. Falls ihr Interesse habt, freue ich mich über eure Nachricht, damit wir gemeinsam eine Lösung finden können.</p>
    <p>✦ Partytime! Vergesst euere Tanzschuhe nicht!</p>
  </div>
</section>

</body>
</html>
```